Need new website for my business

I want to design a new Irrigation website for our business. What we are looking for is to have a residential section that describes providing for irrigation service for residential customers in homeowners Association. From startups to service to winterization in full residential installs.
A commercial section on our webpage describing. installation of commercial Irrigation systems. Service start-up of systems. To winterizations. Offering contract service plans for commercial customers.
Service for both commercial residential include making sure all zones are operating check for leaks adjust spray nozzles in rotors making sure all irrigation heads rotate, and are not stuck or damaged making sure that we have full coverage of each Irrigation zone for lawns. In all drip irrigation is Functioning in watering the plants accordingly. Adjusting control settings to make sure you have the right watering times during the hot dry months.
Have a landscape lighting tab:
Describing what landscape lighting and what it does to enhance curb, appeal, highlight architectural, features of landscape and transferring your outdoor space into inviting visual stunning areas with low-voltage landscape lighting
And a residential snow plowing for the Falmouth Maine area. In commercial snow, plowing and snow removal covering Scarborough south portland Portland Falmouth in Cumberland Maine for commercial Snow services. From plow & Salting parking lots to Snow removing, and Snow displacement.
we started a website but it needs a up lift and bring it to pop
our web site is willowbrookyards314.com
here are a few websites that we really like:
www.sprinklecoastal.com
www.dewpointwatering.com
www.verdantlawnsystems.com
Industry/Entity Type
Irrigation & Landscape Lighting
Coding
Coded - Design and coding required
Number of Pages Required
4 page

```html
<!DOCTYPE html>
<html lang="en">
<head>
<meta charset="utf-8">
<title>Willowbrook Yards — Irrigation, Lighting & Snow Services</title>
<link rel="stylesheet" href="https://fonts.googleapis.com/css2?family=Plus+Jakarta+Sans:wght@500;600;700;800&family=Inter:wght@400;500;600&display=swap">
<style>
:root{
  --green:#1ea51e;
  --green-deep:#0f6b3d;
  --teal:#0e8c80;
  --teal-2:#13987a;
  --blue:#1479c9;
  --navy:#07598a;
  --ice:#e6f4f9;
  --ice-2:#dceff7;
  --ink:#14212b;
  --muted:#4b5862;
  --amber:#f4b223;
  --yellow:#f6c42b;
  --slate:#2f557f;
  --gray-box:#8f9598;
  --footer:#0f2922;
  --white:#ffffff;
}
*{box-sizing:border-box;margin:0;padding:0}
html,body{width:1200px;height:4428px;overflow:hidden}
body{font-family:"Inter",sans-serif;color:var(--ink);background:var(--white);font-size:12px;line-height:1.6}
h1,h2,h3,.brand{font-family:"Plus Jakarta Sans",sans-serif}
.wrap{width:760px;margin:0 auto;position:relative}
section{position:relative;overflow:hidden}

/* nav */
.nav{height:52px;background:#eef8fb;border-bottom:1px solid #d7e8ee}
.nav .wrap{display:flex;align-items:center;height:52px}
.brand{font-weight:800;font-size:19px;color:var(--green);display:flex;align-items:center;gap:6px}
.brand-dot{width:12px;height:12px;border-radius:50%;background:var(--blue)}
.nav-links{display:flex;gap:26px;margin-left:120px;font-size:10px;color:var(--ink);font-weight:500}
.nav-right{margin-left:auto;display:flex;align-items:center;gap:10px;font-size:10px}
.btn{display:inline-flex;align-items:center;gap:8px;font-weight:600;border-radius:3px;font-size:10px;color:#fff;text-decoration:none}
.btn-sm{background:var(--green);padding:6px 8px}

/* hero */
.hero{height:488px}
.hero-photo{position:absolute;inset:0;background:linear-gradient(180deg,#3b4c38 0%,#5b6f3e 45%,#8c9a3a 70%,#4c6b2a 100%)}
.hero-photo::after{content:"";position:absolute;inset:0;background:linear-gradient(90deg,rgba(15,25,20,.65) 0%,rgba(15,25,20,.25) 60%,rgba(0,0,0,0) 100%)}
.hero .wrap{padding-top:70px;color:#fff;z-index:2}
.badges{display:flex;gap:22px;font-size:8px;opacity:.85}
.hero h1{font-size:41px;line-height:1.22;font-weight:800;margin-top:14px}
.hero h1 .hl{color:var(--amber)}
.hero p{font-size:11.5px;width:480px;margin-top:14px;opacity:.9}
.hero-ctas{display:flex;gap:12px;margin-top:44px}
.btn-green{background:var(--green);padding:9px 20px}
.btn-ghost{border:1px solid rgba(255,255,255,.7);padding:8px 20px;background:transparent}

/* intro */
.intro{height:212px;background:var(--ice);text-align:center}
.intro .mark{width:14px;height:14px;background:var(--green);border-radius:50%;margin:22px auto 0}
.intro h2{font-size:28px;font-weight:700;margin-top:14px}
.intro p{width:720px;margin:20px auto 0;font-size:11px;color:#32414b}

/* core */
.core{height:383px;text-align:center}
.core h2{font-size:29px;font-weight:700;margin-top:44px}
.core .sub{font-size:11px;color:var(--muted);margin-top:14px}
.cards{display:flex;gap:16px;margin-top:42px}
.card{width:178px;height:160px;border-radius:4px;color:#fff;text-align:left;padding:18px 21px}
.card .ic{width:40px;height:40px;border-radius:50%;background:rgba(255,255,255,.18);display:flex;align-items:center;justify-content:center}
.card h3{font-size:12px;font-weight:700;margin-top:14px}
.card p{font-size:8.5px;line-height:1.7;margin-top:6px;opacity:.85}
.c1{background:var(--green)}.c2{background:var(--teal-2)}.c3{background:var(--teal)}.c4{background:var(--blue)}

/* irrigation split */
.res{height:471px;background:var(--navy);color:#fff}
.com{height:472px;background:var(--ice-2)}
.split h2{font-size:29px;line-height:1.05;font-weight:700}
.split h2 .hl{color:#33b56b}
.res .wrap{padding-top:66px}
.com .wrap{padding-top:90px}
.split p.lead{width:300px;font-size:10.5px;line-height:1.75;margin-top:22px}
.res p.lead{opacity:.9}
.com p.lead{width:350px;color:#2d3e4a}
.checks{list-style:none;margin-top:14px}
.checks li{display:flex;align-items:center;gap:10px;font-size:9.5px;margin-bottom:7px}
.tick{width:12px;height:12px;border-radius:50%;background:#3fbf5a;flex:none}
.com .tick{background:var(--blue)}
.btn-res{background:var(--green);padding:8px 20px;margin-top:14px}
.btn-com{background:var(--blue);padding:8px 20px;margin-top:16px}
.emblem{position:absolute;left:565px;top:1318px;width:605px;height:605px;border-radius:50%;
  background:radial-gradient(circle,#7cbf62 0 31%,#4f9a86 38%,#1b82b5 50%,rgba(27,130,181,0) 70%);z-index:3}

/* maintenance */
.maint{height:364px;background:var(--ice);text-align:center}
.maint h2{font-size:28px;font-weight:700;margin-top:68px}
.maint h2 .hl{color:var(--green)}
.maint .sub{font-size:11px;color:#2d3e4a;width:420px;margin:6px auto 0;line-height:1.55}
.grid{display:grid;grid-template-columns:repeat(3,244px);gap:14px 14px;margin-top:22px}
.gbox{height:62px;background:var(--gray-box);border:1px solid #70777a;border-radius:3px;display:flex;align-items:center;gap:12px;padding:0 14px;text-align:left;font-size:11px;color:#eef2f3;line-height:1.35}
.gbox .tick{background:transparent;border:1.5px solid #4fd06a}

/* lighting */
.light{height:431px;background:var(--slate);color:#fff}
.light .wrap{padding-top:58px}
.pill{display:inline-block;background:rgba(255,255,255,.16);border-radius:10px;padding:3px 12px;font-size:8px}
.light h2{font-size:36px;line-height:1.1;font-weight:700;margin-top:10px}
.light h2 .hl{color:var(--yellow)}
.light p{width:400px;font-size:10.5px;line-height:1.75;margin-top:14px;opacity:.9}
.dots{display:grid;grid-template-columns:214px 200px;gap:6px 0;margin-top:20px;font-size:9.5px;list-style:none}
.dots li::before{content:"";display:inline-block;width:5px;height:5px;border-radius:50%;background:var(--amber);margin-right:8px;vertical-align:middle}
.btn-amber{background:var(--amber);padding:8px 20px;margin-top:26px}
.lamp-art{position:absolute;left:655px;top:36px;width:360px;height:395px;border-radius:6px;
  background:radial-gradient(ellipse at 50% 30%,#6f9fd8 0%,#4f84c7 45%,rgba(47,85,127,0) 80%)}

/* snow */
.snow{height:658px;color:#fff;text-align:center}
.snow-photo{position:absolute;inset:0;background:linear-gradient(180deg,#3b6fae 0%,#5686c0 30%,#7aa0cd 55%,#c9d7e6 80%,#e9eef5 100%)}
.snow .wrap{z-index:2;padding-top:68px}
.snow .pill{background:none;font-size:8px}
.snow h2{font-size:29px;font-weight:700;margin-top:12px}
.scards{display:flex;gap:22px;justify-content:center;margin-top:30px}
.scard{width:268px;height:202px;background:#0f2a45;border-radius:3px;text-align:left;padding:22px 21px}
.scard .ic{width:30px;height:30px;border-radius:50%;background:rgba(255,255,255,.1)}
.scard h3{font-size:14px;font-weight:700;margin-top:22px}
.scard p{font-size:9.5px;line-height:1.75;margin-top:10px;opacity:.7}
.btn-snow{background:#3d7ebe;padding:7px 20px;margin-top:28px;opacity:.9}

/* reviews */
.reviews{height:377px;text-align:center}
.reviews h2{font-size:29px;font-weight:700;margin-top:80px;color:#163a5a}
.rating{font-size:10px;margin-top:6px;display:flex;justify-content:center;align-items:center;gap:6px}
.stars{color:var(--amber);font-size:14px;letter-spacing:2px}
.rcards{display:flex;gap:14px;margin-top:20px}
.rcard{width:244px;height:132px;border:1px solid #b8c4cc;border-radius:4px;text-align:left;padding:22px 20px;font-size:10px;line-height:1.6}
.rcard .who{font-weight:700;margin-top:12px;font-size:9.5px}
.rcard .loc{font-size:8.5px;color:#8a959c}

/* cta */
.cta{height:301px;background:var(--green-deep);color:#fff;text-align:center}
.cta h2{font-size:36px;font-weight:700;margin-top:82px}
.cta p{font-size:12px;width:420px;margin:12px auto 0;opacity:.9}
.cta-btns{display:flex;gap:14px;justify-content:center;margin-top:26px}
.btn-outline{border:1px solid rgba(255,255,255,.7);padding:7px 40px}

/* footer */
.foot{height:219px;background:var(--footer);color:#e1ece7;font-size:9px}
.foot .cols{display:flex;padding-top:20px}
.foot .about{width:390px}
.foot .about p{margin-top:8px;line-height:1.6;width:280px}
.foot h4{font-size:9.5px;font-weight:600;margin-top:16px}
.foot ul{list-style:none;margin-top:8px;line-height:2}
.foot .col2{width:195px}
.copy{text-align:center;font-size:8px;margin-top:34px;opacity:.8}
</style>
</head>
<body>

<header class="nav">
  <div class="wrap">
    <div class="brand"><span>Willowbrook Yards</span><span class="brand-dot"></span></div>
    <nav class="nav-links"><span>Irrigation</span><span>Lighting</span><span>Snow Services</span><span>About</span></nav>
    <div class="nav-right">
      <svg width="10" height="10" viewBox="0 0 24 24" fill="none" stroke="#14212b" stroke-width="2"><path d="M22 17v4a2 2 0 0 1-2 2A19 19 0 0 1 1 4a2 2 0 0 1 2-2h4l2 5-3 2a12 12 0 0 0 9 9l2-3z"/></svg>
      <span>(207) 555-0148</span>
      <a class="btn btn-sm">Get a Quote</a>
    </div>
  </div>
</header>

<section class="hero">
  <div class="hero-photo" role="img" aria-label="Large home with lush lawn and sprinklers spraying at golden hour"></div>
  <div class="wrap">
    <div class="badges"><span>★ 5-Star Verified Review</span><span>✓ Licensed &amp; Insured</span><span>⌖ Serving Maine Communities</span></div>
    <h1>Premium Irrigation,<br><span class="hl">Landscape Lighting</span><br>&amp; Snow Services in Maine</h1>
    <p>Residential &amp; Commercial Irrigation Systems, Outdoor Lighting &amp; Reliable Snow Management — Designed, Installed &amp; Maintained with Precision.</p>
    <div class="hero-ctas"><a class="btn btn-green">Get Started</a><a class="btn btn-ghost">Request a Free Estimate</a></div>
  </div>
</section>

<section class="intro">
  <div class="mark"></div>
  <h2>Maine's Trusted Irrigation &amp; Outdoor Lighting Experts</h2>
  <p>We specialize in high-performance irrigation systems, low-voltage landscape lighting, and dependable snow services for residential and commercial properties throughout Maine. From system design to seasonal maintenance, our experienced team delivers efficient solutions that protect your landscape and enhance your property year-round.</p>
</section>

<section class="core">
  <h2>Our Core Services</h2>
  <p class="sub">Comprehensive outdoor services designed to enhance and protect your property year-round.</p>
  <div class="wrap cards">
    <div class="card c1"><div class="ic"><svg width="16" height="16" viewBox="0 0 24 24" fill="none" stroke="#fff" stroke-width="2"><path d="M12 3s6 7 6 11a6 6 0 0 1-12 0c0-4 6-11 6-11z"/></svg></div><h3>Irrigation</h3><p>Professional irrigation systems designed for maximum coverage and water efficiency.</p></div>
    <div class="card c2"><div class="ic"><svg width="16" height="16" viewBox="0 0 24 24" fill="none" stroke="#fff" stroke-width="2"><path d="M9 18h6M10 21h4M12 3a6 6 0 0 0-4 10c1 1 1 2 1 3h6c0-1 0-2 1-3a6 6 0 0 0-4-10z"/></svg></div><h3>Landscape Lighting</h3><p>Custom low-voltage lighting that transforms your outdoor spaces.</p></div>
    <div class="card c3"><div class="ic"><svg width="16" height="16" viewBox="0 0 24 24" fill="none" stroke="#fff" stroke-width="2"><path d="M12 2v20M2 12h20M5 5l14 14M19 5 5 19"/></svg></div><h3>Snow Services</h3><p>Reliable snow plowing and removal to keep your property safe all winter.</p></div>
    <div class="card c4"><div class="ic"><svg width="16" height="16" viewBox="0 0 24 24" fill="none" stroke="#fff" stroke-width="2"><rect x="5" y="3" width="14" height="18"/><path d="M9 7h2M13 7h2M9 11h2M13 11h2M9 15h2M13 15h2"/></svg></div><h3>Commercial Contracts</h3><p>Comprehensive service agreements for large properties and businesses.</p></div>
  </div>
</section>

<section class="res split">
  <div class="wrap">
    <h2>Residential <span class="hl">Irrigation</span><br>Services</h2>
    <p class="lead">We provide complete residential irrigation services for homeowners and homeowner associations — from new system installations to seasonal maintenance and winterization. Our systems are designed for maximum coverage, water efficiency, and long-term reliability.</p>
    <ul class="checks">
      <li><span class="tick"></span>Custom irrigation design &amp; installation</li>
      <li><span class="tick"></span>HOA &amp; multi-property systems</li>
      <li><span class="tick"></span>Spring start-ups &amp; inspections</li>
      <li><span class="tick"></span>Repairs &amp; seasonal adjustments</li>
      <li><span class="tick"></span>Professional winterization services</li>
    </ul>
    <a class="btn btn-res">Learn More About Residential Services →</a>
  </div>
</section>

<section class="com split">
  <div class="wrap">
    <h2>Commercial <span class="hl">Irrigation</span><br>Solutions</h2>
    <p class="lead">Our commercial irrigation services support large properties, office parks, condominiums, athletic fields, and municipal spaces. We offer installation, start-ups, winterization, and ongoing service contracts to keep systems operating efficiently year-round.</p>
    <ul class="checks">
      <li><span class="tick"></span>Large-scale system installations</li>
      <li><span class="tick"></span>Seasonal start-ups &amp; shutdowns</li>
      <li><span class="tick"></span>Emergency repairs &amp; inspections</li>
      <li><span class="tick"></span>Commercial service contracts</li>
    </ul>
    <a class="btn btn-com">View Commercial Services →</a>
  </div>
</section>

<div class="emblem" role="img" aria-label="Blue sun-petal emblem framing photos of a home lawn and an athletic field being watered by sprinklers"></div>

<section class="maint">
  <h2>Precision Irrigation <span class="hl">Maintenance</span></h2>
  <p class="sub">Our technicians ensure every irrigation system operates at peak performance — maximizing coverage while reducing water waste.</p>
  <div class="wrap grid">
    <div class="gbox"><span class="tick"></span>Zone testing &amp; coverage verification</div>
    <div class="gbox"><span class="tick"></span>Leak detection &amp; repairs</div>
    <div class="gbox"><span class="tick"></span>Spray nozzle &amp; rotor adjustment</div>
    <div class="gbox"><span class="tick"></span>Head rotation &amp; alignment checks</div>
    <div class="gbox"><span class="tick"></span>Drip irrigation performance testing</div>
    <div class="gbox"><span class="tick"></span>Seasonal controller programming</div>
  </div>
</section>

<section class="light">
  <div class="lamp-art" role="img" aria-label="Illustration of a glowing blue garden path lamp"></div>
  <div class="wrap">
    <span class="pill">✦ Transform Your Nights</span>
    <h2>Low-Voltage <span class="hl">Landscape<br>Lighting</span></h2>
    <p>Landscape lighting enhances curb appeal, highlights architectural features, and transforms outdoor spaces into inviting nighttime environments. Our custom low-voltage lighting designs combine beauty, safety, and energy efficiency.</p>
    <ul class="dots">
      <li>Pathway &amp; accent lighting</li><li>Architectural feature highlighting</li>
      <li>Energy-efficient LED systems</li><li>Custom lighting layouts</li>
    </ul>
    <a class="btn btn-amber">Explore Landscape Lighting →</a>
  </div>
</section>

<section class="snow">
  <div class="snow-photo" role="img" aria-label="Plow truck clearing a snowy parking lot at dusk"></div>
  <div class="wrap">
    <span class="pill">❄ Winter Ready</span>
    <h2>Professional Snow Plowing &amp; Snow Removal</h2>
    <div class="scards">
      <div class="scard"><div class="ic"></div><h3>Residential</h3><p>Residential snow plowing services in Falmouth, Maine, keeping driveways and homes safe all winter.</p></div>
      <div class="scard"><div class="ic"></div><h3>Commercial</h3><p>Commercial snow plowing and removal services across Scarborough, South Portland, Portland, Falmouth, and Cumberland — including plowing, salting, hauling, and snow displacement.</p></div>
    </div>
    <a class="btn btn-snow">Request Snow Services →</a>
  </div>
</section>

<section class="reviews">
  <h2>What Our Customers Are Saying</h2>
  <div class="rating"><span class="stars">★★★★★</span><span>5.0 Verified Review Rating</span></div>
  <div class="wrap rcards">
    <div class="rcard">"Reliable, professional, and efficient from start to finish. Our irrigation system has never worked better."<div class="who">Daniel P.</div><div class="loc">Falmouth, ME</div></div>
    <div class="rcard">"The landscape lighting transformed our home. We get compliments from neighbors every week!"<div class="who">Laura &amp; Ben T.</div><div class="loc">Cumberland, ME</div></div>
    <div class="rcard">"Best snow removal service in the area. They're always on time and thorough."<div class="who">Harbor Office Park</div><div class="loc">Portland, ME</div></div>
  </div>
</section>

<section class="cta">
  <h2>Ready to Get Started?</h2>
  <p>Let us design, install, and maintain your irrigation, lighting, or snow services with precision and care.</p>
  <div class="cta-btns"><a class="btn btn-green">Contact Us Today →</a><a class="btn btn-outline">☏ Call Now</a></div>
</section>

<footer class="foot">
  <div class="wrap">
    <div class="cols">
      <div class="about">
        <div class="brand"><span>Willowbrook Yards</span><span class="brand-dot"></span></div>
        <p>Premium irrigation systems, landscape lighting, and snow services for residential and commercial properties throughout Maine.</p>
        <p><span class="stars" style="font-size:10px">★★★★★</span> 5-Star Verified Review</p>
      </div>
      <div class="col2"><h4>Contact</h4><ul><li>⌖ Serving Southern Maine</li><li>☏ (207) 555-0148</li><li>✉ hello@willowbrookyards314.com</li></ul></div>
      <div><h4>Services</h4><ul style="line-height:1.9"><li>Irrigation Systems</li><li>Landscape Lighting</li><li>Snow Plowing</li><li>Commercial Contracts</li><li>Seasonal Maintenance</li></ul></div>
    </div>
    <div class="copy">© 2026 Willowbrook Yards. All rights reserved. Licensed &amp; Insured.</div>
  </div>
</footer>

</body>
</html>
```